serious, thorough, light and simple - that's my advice and mediations

My business card should combine my logo (uploaded file) and my homepage (https://fellor-mediation.webnestsite.com).

Contact Information for Business Card

Name: Sabine Fellor di Vanti
Phone: 076 412 58 94
mail: sfellor@postkiv.ch
web: www.fellor-di-vanti.ch

```html
<!DOCTYPE html>
<html lang="de">
<head>
<meta charset="utf-8">
<title>Visitenkarte – Sabine Fellor di Vanti</title>
<link rel="stylesheet" href="https://fonts.googleapis.com/css2?family=Arimo:wght@400;700&display=swap">
<style>
  :root {
    --page-bg: #e4e1df;
    --card-blue: #253585;
    --card-light: #f4f1f0;
    --arc-green: #0f6b3a;
    --arc-blush: #e6c7c1;
    --brand-gold: #a98a4e;
    --text-light: #ffffff;
  }
  * { margin: 0; padding: 0; box-sizing: border-box; }
  html, body {
    width: 1200px;
    height: 900px;
    overflow: hidden;
    background: var(--page-bg);
    font-family: "Arimo", Arial, sans-serif;
  }
  .business-card {
    position: absolute;
    left: 100px;
    top: 141px;
    width: 1000px;
    height: 618px;
    background: var(--card-blue);
    overflow: hidden;
    box-shadow: 0 10px 30px rgba(0,0,0,0.18);
  }
  .card-shape {
    position: absolute;
    inset: 0;
    width: 100%;
    height: 100%;
  }
  .holder-name {
    position: absolute;
    left: 60px;
    top: 78px;
    color: var(--text-light);
    font-weight: 700;
    font-size: 29px;
    letter-spacing: 0.2px;
    text-transform: uppercase;
  }
  .contact-list {
    position: absolute;
    left: 58px;
    top: 436px;
    list-style: none;
    color: var(--text-light);
    font-size: 27px;
  }
  .contact-item {
    display: flex;
    align-items: center;
    height: 37px;
  }
  .contact-icon {
    width: 26px;
    height: 26px;
    margin-right: 8px;
    flex: none;
  }
  .brand-name {
    position: absolute;
    left: 553px;
    width: 400px;
    top: 286px;
    text-align: center;
    color: var(--brand-gold);
    font-weight: 400;
    font-size: 31px;
    letter-spacing: 0.5px;
  }
</style>
</head>
<body>
  <div class="business-card">
    <svg class="card-shape" viewBox="0 0 1090 674" preserveAspectRatio="none" aria-hidden="true">
      <circle class="light-panel-edge" cx="836" cy="337" r="347" fill="var(--arc-blush)"/>
      <circle class="light-panel" cx="840" cy="337" r="344" fill="var(--card-light)"/>
      <rect class="light-panel-fill" x="836" y="0" width="254" height="674" fill="var(--card-light)"/>
      <path class="green-arc" d="M 720 32 A 330 330 0 0 0 760 660" fill="none" stroke="var(--arc-green)" stroke-width="9" stroke-linecap="round"/>
    </svg>

    <h1 class="holder-name">Sabine Fellor di Vanti</h1>

    <ul class="contact-list">
      <li class="contact-item">
        <svg class="contact-icon" viewBox="0 0 24 24" aria-hidden="true">
          <path d="M6.6 10.8c1.4 2.8 3.8 5.1 6.6 6.6l2.2-2.2c.3-.3.7-.4 1-.2 1.1.4 2.3.6 3.6.6.6 0 1 .4 1 1V20c0 .6-.4 1-1 1C10.6 21 3 13.4 3 4c0-.6.4-1 1-1h3.5c.6 0 1 .4 1 1 0 1.3.2 2.5.6 3.6.1.3 0 .7-.2 1z" fill="none" stroke="#fff" stroke-width="1.8"/>
          <path d="M14 3.5a6.5 6.5 0 0 1 6.5 6.5M14 7a3 3 0 0 1 3 3" fill="none" stroke="#fff" stroke-width="1.8" stroke-linecap="round"/>
        </svg>
        <span>076 412 58 94</span>
      </li>
      <li class="contact-item">
        <svg class="contact-icon" viewBox="0 0 24 24" aria-hidden="true">
          <rect x="2" y="5" width="20" height="14" fill="#fff"/>
          <path d="M2 5l10 8 10-8M2 19l7-6M22 19l-7-6" fill="none" stroke="var(--card-blue)" stroke-width="1.6"/>
        </svg>
        <span>sfellor@postkiv.ch</span>
      </li>
      <li class="contact-item">
        <svg class="contact-icon" viewBox="0 0 24 24" aria-hidden="true">
          <circle cx="12" cy="12" r="9.5" fill="none" stroke="#fff" stroke-width="1.8"/>
          <ellipse cx="12" cy="12" rx="4" ry="9.5" fill="none" stroke="#fff" stroke-width="1.6"/>
          <path d="M2.5 12h19M4 7h16M4 17h16" fill="none" stroke="#fff" stroke-width="1.6"/>
        </svg>
        <span>www.fellor-di-vanti.ch</span>
      </li>
    </ul>

    <p class="brand-name">Brücken im Gespräch</p>
  </div>
</body>
</html>
```